Fox & Fig honey company needs a label design.

We need a label design for a new honey company, based in the state of Florida called 'Fox & Fig". We are supplying our online customers with the highest quality of the various kinds of raw honey. Our product is honey in the oval hexagon glass jar with black lid. We would like to see designs that use black background with gold font .
In the upper part of the label is gold flying Honey Bee (profile, silhouette). The name of the brand "Fox & Fig" - Caramel font. Additional fonts are Cinzel, Source Sans Pro. Label measurements 2.6" by 3".
Label content:
Fox & Fig
RAW HONEY
wildflower
PURE & NATURAL
made by Florida Bees
foxandfigjars.com
NET WT 12oz (340g)

The final design should have eye catching, luxurious look.
Updates

Need extra days to review

Target Market(s)

Luxury

Industry/Entity Type

Food (bee products)

Font styles to use
Other font styles liked:
• caramel

Colors

Designer to choose colors to be used in the design.

Requirements
Must have
• Gold letters on black background, Drawing of a bee, flying in profile

```html
<!DOCTYPE html>
<html lang="en">
<head>
<meta charset="utf-8">
<title>Fox &amp; Fig Raw Honey Label</title>
<link rel="stylesheet" href="https://fonts.googleapis.com/css2?family=Cinzel:wght@400;500;700&display=swap">
<style>
  :root {
    --page: #ffffff;
    --label-black: #000000;
    --gold: #d9b24a;
    --gold-light: #f0d77f;
    --gold-deep: #a8801f;
    --frame-gold: #b8923a;
  }
  * { box-sizing: border-box; margin: 0; padding: 0; }
  html, body {
    width: 1200px;
    height: 1200px;
    overflow: hidden;
    background: var(--page);
  }
  .canvas {
    position: relative;
    width: 1200px;
    height: 1200px;
  }
  .label {
    position: absolute;
    left: 118px;
    top: 44px;
    width: 962px;
    height: 1110px;
    background: var(--label-black);
    font-family: "Cinzel", serif;
    color: var(--gold);
  }
  .label__frame {
    position: absolute;
    left: 47px;
    top: 56px;
    width: 867px;
    height: 999px;
    border: 1px solid var(--frame-gold);
  }
  .bee-illustration {
    position: absolute;
    left: 72px;
    top: 82px;
    width: 86px;
    height: 104px;
    border-radius: 40% 50% 45% 40%;
    background: radial-gradient(circle at 45% 40%, var(--gold-light), var(--gold-deep));
  }
  .brand-name {
    position: absolute;
    left: 0;
    top: 236px;
    width: 100%;
    text-align: center;
    font-weight: 700;
    font-size: 124px;
    line-height: 1;
    letter-spacing: 2px;
    color: var(--gold);
  }
  .tagline {
    position: absolute;
    top: 406px;
    font-size: 46px;
    line-height: 1;
    font-weight: 400;
    color: var(--gold);
    white-space: nowrap;
  }
  .tagline--left { left: 108px; }
  .tagline--right { right: 98px; }
  .origin {
    position: absolute;
    left: 0;
    top: 530px;
    width: 100%;
    text-align: center;
    font-size: 62px;
    line-height: 1;
    color: var(--gold);
  }
  .variety {
    position: absolute;
    left: 0;
    top: 618px;
    width: 100%;
    text-align: center;
    font-size: 54px;
    line-height: 1;
    color: var(--gold);
  }
  .flower-ornament {
    position: absolute;
    left: 358px;
    top: 684px;
    width: 242px;
    height: 232px;
    border-radius: 50%;
    background: radial-gradient(circle, #2a2210 0%, #4a3a12 55%, #1a1405 100%);
  }
  .website {
    position: absolute;
    left: 0;
    top: 944px;
    width: 100%;
    text-align: center;
    font-size: 54px;
    line-height: 1;
    color: var(--gold);
  }
  .net-weight {
    position: absolute;
    right: 98px;
    top: 1016px;
    font-size: 29px;
    line-height: 1;
    color: var(--gold);
    white-space: nowrap;
  }
</style>
</head>
<body>
<div class="canvas">
  <section class="label">
    <div class="label__frame"></div>
    <div class="bee-illustration" role="img" aria-label="Small gold honey bee flying in profile"></div>
    <h1 class="brand-name">FOX &amp; FIG</h1>
    <p class="tagline tagline--left">PURE &amp; NATURAL</p>
    <p class="tagline tagline--right">RAW HONEY</p>
    <p class="origin">Made by Florida Bees</p>
    <p class="variety">WILDFLOWER</p>
    <div class="flower-ornament" role="img" aria-label="Gold line drawing of a five-petal wildflower"></div>
    <p class="website">FOXANDFIGJARS.COM</p>
    <p class="net-weight">NET WT 12oz (340g)</p>
  </section>
</div>
</body>
</html>
```